Brindle Finance Flyer Design

I would like a high res flyer designed for mass printing. It is for a mortgage and finance broking company in Sydney. We are called Brindle Finance. The wording i would like displayed is the following
Looking For Something Extra from your broker?
Brindle Finance can make all the difference
What we offer you is an extensive range of mortgage and finance products, including:
• Home Loans
• Investment Loans
• Low Doc Loans
• Vehicle Finance
• Equipment Finance
• Commercial Loans
• Refinance
Contact Us
Phone (02) 7412 5830
email info@brindlefinance.com.au
web www.brindlefinance.com.au
Industry/Entity Type
Finance
Look and feel

```html
<!DOCTYPE html>
<html lang="en">
<head>
<meta charset="utf-8">
<title>Brindle Finance Flyer</title>
<link rel="stylesheet" href="https://fonts.googleapis.com/css2?family=Anton&family=Open+Sans:wght@400;600&family=Ubuntu:wght@400;500;700&display=swap">
<style>
  :root {
    --stage: #1d1d1f;
    --royal: #1d3fb0;
    --royal-deep: #16308c;
    --navy-text: #1a3591;
    --amber: #f4ad1e;
    --silver-light: #f4f4f5;
    --silver-mid: #cfd0d3;
    --ink: #111;
    --white: #fff;
  }
  * { box-sizing: border-box; margin: 0; padding: 0; }
  html, body { width: 913px; height: 1200px; overflow: hidden; background: var(--stage); }
  .flyer {
    position: absolute; left: 62px; top: 62px;
    width: 791px; height: 1078px; overflow: hidden; background: var(--white);
    font-family: "Ubuntu", sans-serif;
  }
  .flyer-shapes { position: absolute; inset: 0; }
  .brand { position: absolute; left: 420px; top: 44px; width: 360px; }
  .brand-name {
    display: flex; align-items: center; gap: 12px;
    font-family: "Open Sans", sans-serif; font-weight: 400; font-size: 36px; color: #222; line-height: 1;
  }
  .brand-square { width: 30px; height: 30px; background: #222; flex: none; }
  .brand-tagline {
    font-family: "Open Sans", sans-serif; font-size: 12.5px; color: #333; margin: 6px 0 0 42px;
  }
  .offer { position: absolute; right: 33px; top: 506px; text-align: right; }
  .offer-title {
    font-family: "Anton", sans-serif; font-size: 38px; color: var(--amber);
    letter-spacing: .5px; line-height: 44px; margin-right: 12px; margin-bottom: 2px;
  }
  .offer-list { list-style: none; }
  .offer-list li { font-size: 26px; color: var(--white); line-height: 34.7px; }
  .offer-list li::after {
    content: ""; display: inline-block; width: 10px; height: 10px; border-radius: 50%;
    background: var(--amber); margin-left: 10px; vertical-align: 3px;
  }
  .headline { position: absolute; left: 24px; top: 608px; }
  .headline-lead { font-weight: 700; font-size: 66px; color: var(--navy-text); line-height: 67px; }
  .headline-sub { font-weight: 500; font-size: 42px; color: var(--ink); line-height: 46px; }
  .headline-question { font-weight: 500; font-size: 32px; color: var(--ink); line-height: 44px; }
  .promise { position: absolute; left: 24px; top: 802px; }
  .promise-name {
    font-family: "Anton", sans-serif; font-size: 74px; color: var(--navy-text);
    line-height: 74px; text-shadow: 2px 3px 3px rgba(0,0,0,.3);
  }
  .promise-line {
    font-family: "Anton", sans-serif; font-size: 54px; color: var(--amber);
    line-height: 60px; margin-top: 10px; text-shadow: 1px 2px 2px rgba(0,0,0,.25);
  }
  .contact {
    position: absolute; left: 0; right: 0; top: 1004px;
    display: flex; justify-content: space-between; padding: 0 18px 0 20px;
    font-size: 20px; line-height: 28px; color: var(--white);
  }
  .contact-item { display: flex; align-items: center; gap: 8px; }
  .contact-item svg { width: 17px; height: 17px; }
</style>
</head>
<body>
<main class="flyer">
  <svg class="flyer-shapes" viewBox="0 0 791 1078" width="791" height="1078">
    <defs>
      <linearGradient id="office-tones" x1="0" y1="0" x2="1" y2="1">
        <stop offset="0" stop-color="#dfe6ef"/>
        <stop offset=".35" stop-color="#f3f6fa"/>
        <stop offset=".7" stop-color="#e8edf4"/>
        <stop offset="1" stop-color="#cfd8e6"/>
      </linearGradient>
      <radialGradient id="figure-tones" cx=".25" cy=".3" r=".45">
        <stop offset="0" stop-color="#2a3f78"/>
        <stop offset=".6" stop-color="#5a6c98" stop-opacity=".6"/>
        <stop offset="1" stop-color="#e6ebf2" stop-opacity="0"/>
      </radialGradient>
      <linearGradient id="silver" x1="0" y1="0" x2="1" y2="1">
        <stop offset="0" stop-color="var(--silver-mid)"/>
        <stop offset=".45" stop-color="var(--silver-light)"/>
        <stop offset="1" stop-color="var(--silver-mid)"/>
      </linearGradient>
      <linearGradient id="royal-panel" x1="0" y1="0" x2="1" y2="1">
        <stop offset="0" stop-color="#2552cc"/>
        <stop offset="1" stop-color="var(--royal-deep)"/>
      </linearGradient>
      <linearGradient id="footer-band" x1="0" y1="0" x2="0" y2="1">
        <stop offset="0" stop-color="#2350c6"/>
        <stop offset="1" stop-color="var(--royal-deep)"/>
      </linearGradient>
    </defs>

    <g role="img" aria-label="Blurred photo of business people walking through a bright office">
      <rect width="791" height="1078" fill="url(#office-tones)"/>
      <rect width="791" height="700" fill="url(#figure-tones)"/>
    </g>

    <!-- logo header band -->
    <path d="M388,0 H791 V104 C700,130 560,170 452,184 C424,187 414,160 418,128 Z" fill="url(#silver)"/>
    <path d="M430,168 C470,186 560,172 791,112" fill="none" stroke="var(--royal)" stroke-width="5"/>

    <!-- lower left silver area -->
    <path d="M0,398 L396,656 Q434,682 444,714 L722,966 H0 Z" fill="var(--white)"/>
    <path d="M0,393 L400,650 Q440,676 452,712 L730,966" fill="none" stroke="var(--amber)" stroke-width="4"/>
    <path d="M0,468 L378,680 Q424,700 436,714 L712,966" fill="none" stroke="var(--royal)" stroke-width="5"/>
    <path d="M0,478 L374,690 Q418,708 428,720 L702,966 H0 Z" fill="url(#silver)"/>

    <!-- right offer panel -->
    <path d="M791,128 L458,604 Q420,662 452,714 L740,966 H791 Z" fill="var(--white)"/>
    <path d="M791,128 L458,604 Q420,662 452,714 L736,966" fill="none" stroke="var(--amber)" stroke-width="4"/>
    <path d="M791,112 L470,582" fill="none" stroke="var(--royal)" stroke-width="6"/>
    <path d="M791,150 L478,612 Q440,668 470,712 L752,966 H791 Z" fill="url(#royal-panel)"/>

    <!-- footer -->
    <rect y="966" width="791" height="112" fill="url(#footer-band)"/>
    <rect y="964" width="791" height="4" fill="var(--amber)"/>
  </svg>

  <header class="brand">
    <div class="brand-name"><span class="brand-square"></span>Brindle Finance</div>
    <p class="brand-tagline">mortgage and finance broking services</p>
  </header>

  <section class="offer">
    <h2 class="offer-title">WE OFFER</h2>
    <ul class="offer-list">
      <li>Home Loans</li>
      <li>Investment Loans</li>
      <li>Low Doc Loans</li>
      <li>Vehicle Finance</li>
      <li>Equipment Finance</li>
      <li>Commercial Loans</li>
      <li>Refinance</li>
    </ul>
  </section>

  <section class="headline">
    <h1 class="headline-lead">Looking</h1>
    <p class="headline-sub">For Something</p>
    <p class="headline-question">Extra from your broker?</p>
  </section>

  <section class="promise">
    <p class="promise-name">Brindle Finance</p>
    <p class="promise-line">can make all the difference</p>
  </section>

  <footer class="contact">
    <span class="contact-item">
      <svg viewBox="0 0 24 24"><path d="M6.6 10.8a15 15 0 0 0 6.6 6.6l2.2-2.2a1 1 0 0 1 1-.25 11.4 11.4 0 0 0 3.6.57 1 1 0 0 1 1 1V20a1 1 0 0 1-1 1A17 17 0 0 1 3 4a1 1 0 0 1 1-1h3.5a1 1 0 0 1 1 1c0 1.25.2 2.45.57 3.57a1 1 0 0 1-.25 1z" fill="var(--amber)"/></svg>
      (02) 7412 5830
    </span>
    <span class="contact-item">
      <svg viewBox="0 0 24 24"><rect x="2" y="5" width="20" height="14" fill="var(--amber)"/><path d="M2 5l10 8 10-8" fill="none" stroke="var(--royal)" stroke-width="1.6"/></svg>
      info@brindlefinance.com.au
    </span>
    <span class="contact-item">
      <svg viewBox="0 0 24 24"><circle cx="12" cy="12" r="10" fill="var(--amber)"/><path d="M2 12h20M12 2c3 3 3 17 0 20M12 2c-3 3-3 17 0 20M4 7h16M4 17h16" fill="none" stroke="var(--royal)" stroke-width="1.2"/></svg>
      www.brindlefinance.com.au
    </span>
  </footer>
</main>
</body>
</html>
```